Sumvera financial services stationery design

We need business stationery designed with letterheads, business cards, with compliments and envelope for a business that offers tax and accounting services
Updates

Designs look the same

Target Market(s)

Small to medium businesses, individuals, Self managed superfunds

Industry/Entity Type

Business

Font styles to use
Serif
Other font styles liked:
• Atlanta

Colors
32a6d6
3277b5

Requirements
Must have
• Logo incorporated with all my stationery
• professional
Should not have
• Lots of colours
• Busy

```html
<!DOCTYPE html>
<html lang="en">
<head>
<meta charset="utf-8">
<title>Sumvera Financial Services – Stationery</title>
<link rel="stylesheet" href="https://fonts.googleapis.com/css2?family=Questrial&display=swap">
<style>
  :root{
    --bg:#dcdddf;
    --paper:#ffffff;
    --ink:#222428;
    --muted:#6b6d70;
    --blue:#3277b5;
    --sky:#32a6d6;
    --grey:#a6a7a9;
    --rule:#c9cacc;
  }
  *{margin:0;padding:0;box-sizing:border-box}
  html,body{width:1200px;height:900px;overflow:hidden;background:var(--bg)}
  body{position:relative;font-family:"Questrial",Arial,sans-serif;color:var(--ink)}
  .sheet{position:absolute;background:var(--paper)}
  .brand{position:absolute;display:flex;align-items:center;gap:8px}
  .brand-square{width:26px;height:26px;background:var(--blue)}
  .brand-name{font-size:24px;color:var(--muted);letter-spacing:1px}
  .edge-bar{position:absolute;left:0;width:100%;height:10px;display:block}

  /* letterhead */
  .letterhead{left:64px;top:82px;width:496px;height:702px}
  .letterhead .brand{left:327px;top:40px}
  .letter{position:absolute;left:50px;top:134px;width:396px;font-size:7.4px;line-height:13.3px}
  .letter p{margin-bottom:13.3px;text-align:justify}
  .letter .date{margin-bottom:13.3px}
  .letter .recipient{margin-bottom:13.3px}
  .letter .subject{font-weight:bold;margin-bottom:13.3px}
  .signature{width:72px;height:18px;background:linear-gradient(90deg,#f1f1f1,#e4e4e4);border-radius:9px;margin-bottom:2px}
  .signer strong{font-weight:bold}
  .footer-contact{position:absolute;left:50px;top:659px;width:396px;display:flex;justify-content:space-between;font-size:7.4px;line-height:12px}
  .footer-contact .addr{text-align:right}
  .contact-line{display:flex;align-items:center;gap:5px}
  .contact-line svg{width:7px;height:7px;flex:none}
  .letterhead .edge-bar{top:692px}

  /* envelope */
  .envelope-front{left:603px;top:82px;width:533px;height:233px}
  .envelope-front .brand,.compliment .brand{left:39px;top:44px}
  .address-window{position:absolute;left:313px;top:39px;width:186px;height:81px;border:1px solid #e7e8e9;border-radius:4px}
  .contact-block{position:absolute;left:39px;top:161px;width:198px;font-size:7.4px;line-height:12px}
  .contact-cols{display:flex;gap:60px;padding-bottom:7px;border-bottom:1px solid var(--rule)}
  .contact-block .addr{margin-top:7px}
  .envelope-front .edge-bar{top:224px}
  .envelope-back{left:603px;top:326px;width:533px;height:232px}
  .flap{position:absolute;left:0;top:0;width:533px;height:56px}
  .back-mark{position:absolute;left:254px;top:174px;width:26px;height:26px;background:var(--blue)}

  /* with compliments */
  .compliment{left:603px;top:584px;width:533px;height:232px}
  .compliment-title{position:absolute;right:42px;top:46px;font-size:14px;letter-spacing:1.5px;color:var(--muted)}
  .compliment .edge-bar{top:222px}
</style>
</head>
<body>

<svg width="0" height="0" style="position:absolute" aria-hidden="true">
  <defs>
    <symbol id="icon-phone" viewBox="0 0 10 10"><path d="M2 1l2 2-1 1c.6 1.3 1.6 2.3 3 3l1-1 2 2-1.5 1.5C4 9 1 6 .5 2.5z" fill="#8a8c8f"/></symbol>
    <symbol id="icon-mobile" viewBox="0 0 10 10"><rect x="2.5" y=".5" width="5" height="9" rx="1" fill="none" stroke="#8a8c8f"/></symbol>
    <symbol id="icon-mail" viewBox="0 0 10 10"><rect x=".5" y="2" width="9" height="6" fill="#8a8c8f"/><path d="M.5 2l4.5 3.5L9.5 2" stroke="#fff" fill="none" stroke-width=".8"/></symbol>
    <symbol id="icon-web" viewBox="0 0 10 10"><circle cx="5" cy="5" r="4.5" fill="#8a8c8f"/><path d="M.5 5h9M5 .5c-2 2.5-2 6.5 0 9M5 .5c2 2.5 2 6.5 0 9" stroke="#fff" fill="none" stroke-width=".6"/></symbol>
  </defs>
</svg>

<!-- Letterhead -->
<section class="sheet letterhead">
  <div class="brand"><span class="brand-square"></span><span class="brand-name">Sumvera</span></div>

  <div class="letter">
    <div class="date">31 December 2018</div>
    <div class="recipient">Martin Keller<br>Director<br>Linden Avenue<br>Fairview 104</div>
    <div class="subject">Praesent dignissim risus tellus, at congue orci tempus id</div>
    <p>Integer feugiat risus purus, vel cursus sem finibus sed. Nulla rhoncus erat non sem pulvinar maximus. In sed viverra urna. Mauris euismod varius felis quis porttitor. Duis facilisis nisi id nisl dignissim, in cursus sem finibus. Nam viverra neque in cursus interdum. Nullam consectetur ipsum quis cursus dignissim. Praesent dignissim risus tellus, at congue orci tempus id. Vivamus ullamcorper mattis dui vitae dictum.</p>
    <p>Suspendisse iaculis pellentesque lorem. Donec eget risus fermentum, consequat dui quis, rutrum quam. Sed et enim ac nisi fringilla condimentum id sed neque. Sed eget imperdiet mauris. Integer ultricies libero quis nulla auctor, venenatis faucibus ipsum aliquet. Etiam faucibus justo leo, sit amet ultrices ipsum dignissim eget. In hac habitasse platea dictumst. Nullam feugiat neque ac velit scelerisque lacinia eu at est. Morbi tincidunt lorem sed dolor commodo lobortis.</p>
    <p>Maecenas non est a lectus bibendum dignissim. Nam ex neque, euismod in suscipit non, cursus non justo. Duis fringilla vulputate magna, sed iaculis felis vehicula nec. Aenean ut tempor orci. Fusce sagittis tincidunt odio non tristique. In sit amet malesuada ex. Suspendisse sed sapien a nunc facilisis porttitor. Etiam ullamcorper varius metus, nec pellentesque ante porta sit amet. Vestibulum efficitur nulla et sapien congue, non sollicitudin massa mollis. Fusce mattis rutrum condimentum. Fusce rutrum semper arcu, ac pretium urna venenatis quis. Integer sed pharetra nulla. Nullam eleifend metus eu gravida euismod. Mauris sit amet scelerisque tortor, vel finibus massa. Sed eget dui semper nisi porttitor viverra.</p>
    <div class="signature" role="img" aria-label="Handwritten signature"></div>
    <div class="signer"><strong>Laura Benson</strong><br>Director<br>Sumvera - Company name</div>
  </div>

  <div class="footer-contact">
    <div>
      <div class="contact-line"><svg><use href="#icon-phone"/></svg>212.555.0148</div>
      <div class="contact-line"><svg><use href="#icon-mobile"/></svg>646.555.0193</div>
    </div>
    <div>
      <div class="contact-line"><svg><use href="#icon-mail"/></svg>hello@sumvera.com</div>
      <div class="contact-line"><svg><use href="#icon-web"/></svg>www.sumvera.com</div>
    </div>
    <div class="addr">Linden Avenue<br>Fairview, NY 104</div>
  </div>

  <svg class="edge-bar" viewBox="0 0 496 10" preserveAspectRatio="none" aria-hidden="true">
    <polygon points="0,0 428,0 434,10 0,10" fill="var(--blue)"/>
    <polygon points="433,0 496,0 496,10 439,10" fill="var(--grey)"/>
  </svg>
</section>

<!-- Envelope front -->
<section class="sheet envelope-front">
  <div class="brand"><span class="brand-square"></span><span class="brand-name">Sumvera</span></div>
  <div class="address-window"></div>
  <div class="contact-block">
    <div class="contact-cols">
      <div>
        <div class="contact-line"><svg><use href="#icon-phone"/></svg>212.555.0148</div>
        <div class="contact-line"><svg><use href="#icon-mobile"/></svg>646.555.0193</div>
      </div>
      <div>
        <div class="contact-line"><svg><use href="#icon-mail"/></svg>hello@sumvera.com</div>
        <div class="contact-line"><svg><use href="#icon-web"/></svg>www.sumvera.com</div>
      </div>
    </div>
    <div class="addr">Linden Avenue, Fairview, NY 104</div>
  </div>
  <svg class="edge-bar" viewBox="0 0 533 10" preserveAspectRatio="none" aria-hidden="true">
    <polygon points="0,0 458,0 464,10 0,10" fill="var(--blue)"/>
    <polygon points="463,0 533,0 533,10 469,10" fill="var(--grey)"/>
  </svg>
</section>

<!-- Envelope back -->
<section class="sheet envelope-back">
  <svg class="flap" viewBox="0 0 533 56" aria-hidden="true">
    <path d="M0 0H533L528 46Q527 56 517 56H16Q6 56 5 46Z" fill="var(--sky)"/>
  </svg>
  <span class="back-mark"></span>
</section>

<!-- With compliments -->
<section class="sheet compliment">
  <div class="brand"><span class="brand-square"></span><span class="brand-name">Sumvera</span></div>
  <div class="compliment-title">WITH COMPLIMENT</div>
  <div class="contact-block">
    <div class="contact-cols">
      <div>
        <div class="contact-line"><svg><use href="#icon-phone"/></svg>212.555.0148</div>
        <div class="contact-line"><svg><use href="#icon-mobile"/></svg>646.555.0193</div>
      </div>
      <div>
        <div class="contact-line"><svg><use href="#icon-mail"/></svg>hello@sumvera.com</div>
        <div class="contact-line"><svg><use href="#icon-web"/></svg>www.sumvera.com</div>
      </div>
    </div>
    <div class="addr">Linden Avenue, Fairview, NY 104</div>
  </div>
  <svg class="edge-bar" viewBox="0 0 533 10" preserveAspectRatio="none" aria-hidden="true">
    <polygon points="0,0 458,0 464,10 0,10" fill="var(--blue)"/>
    <polygon points="463,0 533,0 533,10 469,10" fill="var(--grey)"/>
  </svg>
</section>

</body>
</html>
```